Mobile Recording Studio needs business cards

Open to seeing a creative design, but I want to emphasis my logo and minimize the name/title and company information. Possible a fully black background on card.

My company is a mobile sound recording studio. ok to include a my trailer (actual or cartoon) on the card. My initial thought is more straight forward, but a good design will win me over.

SPECS:
CMYK color mode
High (300ppi) raster effect.
cover bleed area
please deliver: Illustrator file with layers and a pdf at completion.

Name and info for the business card:

Dallin Perry
ADR Mixer

email: Dallin@MixVault.com

address:
248 - 5170 East Hollister
Vancouver, BC V5R 2J4

phone:
604.518.2093 office

website:
www.MixVault.com

FB: @MixVault

Instagram: @TheMixVault

Industry/Entity Type

Television Production

Contact Information for Business Card

Dallin Perry
ADR Mixer

email: Dallin@MixVault.com

address:
248 - 5170 East Hollister
Vancouver, BC V5R 2J4

phone:
604.518.2093 office

website:
www.MixVault.com

FB: @MixVault

Instagram: @TheMixVault

Colors

Designer to choose colors to be used in the design.

Requirements
Must have
• emphasis my logo and minimize the name/title and company information.
• SPECS:
• CMYK color mode
• High (300ppi) raster effect.
• cover bleed area
• please deliver: Illustrator file with layers and a pdf at completion.
Nice to have
• maybe include the following:
• all black background or black theme
• my work trailer (actual or cartoon) refer to Instagram: @TheMixVault

```html
<!DOCTYPE html>
<html lang="en">
<head>
<meta charset="utf-8">
<title>MixVault Business Cards</title>
<link href="https://fonts.googleapis.com/css2?family=Montserrat:wght@400;500;600&display=swap" rel="stylesheet">
<style>
  :root {
    --backdrop: #6b5640;
    --card-black: #050505;
    --card-grey-top: #5c5c5c;
    --card-grey-bottom: #3a3a3a;
    --text-white: #ffffff;
    --text-muted: #9a9a9a;
    --silver: #cfcfcf;
    --band: #8a8a8a;
    --icon: #8c8c8c;
    --icon-ink: #111111;
  }
  * { margin: 0; padding: 0; box-sizing: border-box; }
  html, body { width: 900px; height: 1200px; overflow: hidden; }
  body {
    position: relative;
    background: var(--backdrop);
    font-family: "Montserrat", Arial, sans-serif;
  }
  .card {
    position: absolute;
    left: 80px;
    width: 732px;
    height: 428px;
    border-radius: 22px;
    overflow: hidden;
  }
  .card-front { top: 128px; background: var(--card-black); color: var(--text-white); }
  .card-back {
    top: 646px;
    background: linear-gradient(180deg, var(--card-grey-top) 0%, var(--card-grey-bottom) 100%);
  }

  .person { position: absolute; left: 48px; top: 48px; }
  .person-name { font-size: 20px; font-weight: 500; letter-spacing: 0.5px; line-height: 24px; }
  .person-role { font-size: 15px; color: var(--text-muted); line-height: 20px; }

  .contact-list { position: absolute; left: 48px; top: 228px; list-style: none; }
  .contact-item { display: flex; align-items: center; height: 30px; font-size: 16px; line-height: 20px; }
  .contact-icon { width: 20px; height: 20px; margin-right: 12px; flex: none; }

  .address {
    position: absolute; left: 0; right: 0; top: 390px;
    text-align: center; font-size: 16px; font-weight: 500; line-height: 20px;
  }

  .brand-mark {
    position: absolute;
    font-weight: 600;
    color: var(--silver);
    letter-spacing: 2px;
    text-align: center;
    line-height: 1;
  }
  .card-front .brand-mark { left: 380px; top: 156px; width: 320px; font-size: 46px; }
  .card-back .brand-mark { left: 0; right: 0; top: 176px; font-size: 96px; }

  .back-band {
    position: absolute; left: 0; right: 0; top: 364px; height: 64px;
    background: linear-gradient(180deg, #6e6e6e 0%, #4a4a4a 100%);
    border-top: 2px solid var(--band);
  }
</style>
</head>
<body>

<section class="card card-front">
  <div class="person">
    <div class="person-name">DALLIN PERRY</div>
    <div class="person-role">ADR Mixer</div>
  </div>

  <ul class="contact-list">
    <li class="contact-item">
      <svg class="contact-icon" viewBox="0 0 20 20" aria-hidden="true">
        <circle cx="10" cy="10" r="10" fill="var(--icon)"/>
        <path d="M6 7.5c0-1 1.5-1.8 4-1.8s4 .8 4 1.8v.8h-2.2v-1h-3.6v1H6z M7 9.5h6l1 4.5H6z" fill="var(--icon-ink)"/>
      </svg>
      604.518.2093 (OFFICE)
    </li>
    <li class="contact-item">
      <svg class="contact-icon" viewBox="0 0 20 20" aria-hidden="true">
        <circle cx="10" cy="10" r="10" fill="var(--icon)"/>
        <g fill="none" stroke="var(--icon-ink)" stroke-width="1.2">
          <rect x="4.5" y="6" width="11" height="8" rx="1"/>
          <path d="M4.8 6.5 10 10.5l5.2-4"/>
        </g>
      </svg>
      Dallin@MixVault.com
    </li>
    <li class="contact-item">
      <svg class="contact-icon" viewBox="0 0 20 20" aria-hidden="true">
        <circle cx="10" cy="10" r="10" fill="var(--icon)"/>
        <g fill="none" stroke="var(--icon-ink)" stroke-width="1.2">
          <circle cx="10" cy="10" r="5.5"/>
          <ellipse cx="10" cy="10" rx="2.4" ry="5.5"/>
          <line x1="4.5" y1="10" x2="15.5" y2="10"/>
        </g>
      </svg>
      www.MixVault.com
    </li>
    <li class="contact-item">
      <svg class="contact-icon" viewBox="0 0 20 20" aria-hidden="true"><circle cx="10" cy="10" r="10" fill="var(--icon)"/></svg>
      @MixVault
    </li>
    <li class="contact-item">
      <svg class="contact-icon" viewBox="0 0 20 20" aria-hidden="true"><circle cx="10" cy="10" r="10" fill="var(--icon)"/></svg>
      @TheMixVault
    </li>
  </ul>

  <div class="brand-mark">MIXVAULT</div>

  <div class="address">248 - 5170 East Hollister, Vancouver, BC V5R 2J4</div>
</section>

<section class="card card-back">
  <div class="brand-mark">MIXVAULT</div>
  <div class="back-band"></div>
</section>

</body>
</html>
```